TriVex Business Card Design - double sided -plumbing local plumbing company

We have a Plumbing company where the design was create through Sketch Hive. We would now like a business card designed as well. We want it to be in the colour version of the logo.

Details below for the card.

Phone Number: 0438 615 247
Email: info@trivexplumbing.example.au
Website: https://trivexplumbing.example.au
We really want a sophisticated design that stand out from the other- informative and timeless.

Target Market(s)

local Canberra market

Industry/Entity Type

Plumbing, gas fitting, hot water

Contact Information for Business Card

Phone number, email, logo and "Supplying all your heating, cooling and hot water needs"

Requirements
Must have
• bust be colourful, must also be though about it being printed on a magnet. must Vex with the logo - I dont want the logo and information chucked onto a white canvas I would prefer it to be smooth and look purposeful

```html
<!DOCTYPE html>
<html lang="en">
<head>
<meta charset="utf-8">
<title>TriVex Business Card</title>
<link href="https://fonts.googleapis.com/css2?family=Lato:wght@400;700;900&display=swap" rel="stylesheet">
<style>
  :root {
    --brand-blue: #00aeef;
    --brand-orange: #fbb040;
    --ink: #1c1c1c;
    --paper: #ffffff;
    --backdrop: #f3f3f3;
  }
  * { margin: 0; padding: 0; box-sizing: border-box; }
  html, body { width: 962px; height: 1200px; overflow: hidden; }
  body {
    background: var(--backdrop);
    font-family: "Lato", sans-serif;
    position: relative;
  }
  .card {
    position: absolute;
    left: 106px;
    width: 750px;
    height: 429px;
    background: var(--paper);
    overflow: hidden;
  }
  .card--front { top: 122px; }
  .card--back { top: 649px; }

  .wordmark {
    position: absolute;
    display: flex;
    align-items: center;
    gap: 14px;
    font-weight: 900;
    font-size: 88px;
    line-height: 1;
    letter-spacing: 4px;
    color: var(--brand-blue);
    text-transform: uppercase;
  }
  .wordmark__dot {
    width: 56px;
    height: 56px;
    border-radius: 50%;
    background: var(--brand-orange);
    flex: none;
  }
  .card--front .wordmark { left: 256px; top: 44px; }
  .card--back .wordmark { left: 50%; top: 154px; transform: translateX(-50%); }

  .holder { position: absolute; left: 41px; top: 174px; }
  .holder__name {
    font-weight: 700;
    font-size: 28px;
    color: var(--brand-blue);
    letter-spacing: 0.2px;
  }
  .holder__role {
    font-weight: 700;
    font-size: 17px;
    color: var(--brand-orange);
    margin-top: 2px;
  }

  .company {
    position: absolute;
    left: 426px;
    top: 177px;
    font-size: 16.5px;
    line-height: 21px;
    color: var(--ink);
  }
  .contacts {
    position: absolute;
    left: 426px;
    top: 232px;
    list-style: none;
    font-size: 19px;
    color: var(--ink);
  }
  .contacts li {
    display: flex;
    align-items: center;
    gap: 10px;
    height: 28px;
    white-space: nowrap;
  }
  .contacts svg { width: 13px; height: 13px; flex: none; }

  .front-artwork {
    position: absolute;
    left: 0;
    top: 330px;
    width: 100%;
    height: 99px;
    background: linear-gradient(to bottom, var(--brand-orange) 0%, var(--brand-blue) 45%, var(--brand-blue) 100%);
  }

  .tagline-band {
    position: absolute;
    left: 0;
    top: 293px;
    width: 100%;
    height: 80px;
    background: var(--brand-blue);
    display: flex;
    align-items: center;
    justify-content: center;
    color: var(--paper);
    font-weight: 700;
    font-size: 22.5px;
  }
</style>
</head>
<body>

<section class="card card--front">
  <div class="front-artwork" role="img" aria-label="Decorative blue and orange flowing wave artwork along the bottom of the card"></div>

  <div class="wordmark"><span class="wordmark__dot"></span>TriVex</div>

  <div class="holder">
    <p class="holder__name">MARTIN K DALLOW</p>
    <p class="holder__role">Harbour</p>
  </div>

  <p class="company">Harbour Industrial SuppliesLL<br>C207&nbsp; B 4831Harbour Industria</p>

  <ul class="contacts">
    <li>
      <svg viewBox="0 0 16 16" aria-hidden="true"><circle cx="8" cy="8" r="8" fill="#00aeef"/><path d="M5 4.5l1.6-.4 1 2-1 .8c.4 1 1.2 1.8 2.2 2.2l.8-1 2 1-.4 1.6c-3.2 0-6.2-3-6.2-6.2z" fill="#fff"/></svg>
      0438 615 247
    </li>
    <li>
      <svg viewBox="0 0 16 16" aria-hidden="true"><circle cx="8" cy="8" r="7" fill="none" stroke="#00aeef" stroke-width="2"/><path d="M1 8h14M8 1c-3 3-3 11 0 14M8 1c3 3 3 11 0 14" fill="none" stroke="#00aeef" stroke-width="1.3"/></svg>
      https://trivexplumbing.example.au
    </li>
    <li>
      <svg viewBox="0 0 16 16" aria-hidden="true"><rect x="1" y="3.5" width="14" height="9" fill="#00aeef"/><path d="M1 3.5l7 5 7-5" fill="none" stroke="#fff" stroke-width="1.2"/></svg>
      info@trivexplumbing.example.au
    </li>
  </ul>
</section>

<section class="card card--back">
  <div class="wordmark"><span class="wordmark__dot"></span>TriVex</div>
  <p class="tagline-band">"Supplying all your heating, cooling and hot water needs"</p>
</section>

</body>
</html>
```